Corporate Two Sided Business Card

Looking for a Corporate "edgy" Modern look and feel for a business card

We are looking at two options. Dark background with our logo on it, white background with our logo on it - The background is more - Charcoal / Graphite then black

Details will be

Danielle Forsk

Licensee / Director

m. 0428 519 064

e. danielle@quorvela.com.au

quorvela.com.au

Target Market(s)

Professional Business people that refer use business and clients that own Investment Properties

Industry/Entity Type

Business

Contact Information for Business Card

Details will be

Danielle Forsk

Licensee / Director

m. 0428 519 064

quorvela.com.au

Font styles to use
Serif

Colors
000000
ec1f27
eeeeee
ffffff

Requirements
Must have
• Two options - White Background and Dark Background. - Two sided
Nice to have
• A design that is edgy, modern and new to look instead of boring style corporate cards - It should be a full integrated design
Should not have
• Block looking - Cheap.

```html
<!DOCTYPE html>
<html lang="en">
<head>
<meta charset="utf-8">
<title>Quorvela Business Card</title>
<link rel="stylesheet" href="https://fonts.googleapis.com/css2?family=Quicksand:wght@400;500;700&display=swap">
<style>
  :root {
    --red: #ec1f27;
    --charcoal: #2b2b2d;
    --graphite: #3a3a3d;
    --wordmark-grey: #5d5d62;
    --text-grey: #555558;
    --paper: #ffffff;
    --backdrop: #eeeeee;
  }
  * { margin: 0; padding: 0; box-sizing: border-box; }
  html, body {
    width: 1200px; height: 1200px; overflow: hidden;
    background: var(--backdrop);
    font-family: "Quicksand", sans-serif;
  }
  .sheet {
    position: relative; width: 1200px; height: 1200px;
  }
  .card {
    position: absolute; left: 220px; width: 760px; height: 434px;
    box-shadow: 0 10px 28px rgba(0,0,0,.18);
    overflow: hidden;
  }
  /* Dark side */
  .card--dark {
    top: 110px;
    background: linear-gradient(120deg, var(--graphite) 0%, var(--charcoal) 55%, #222224 100%);
  }
  .card--dark .base-band {
    position: absolute; left: 0; right: 0; bottom: 0; height: 38px;
    background: var(--red);
  }
  .card--dark .brand {
    position: absolute; left: 0; right: 0; top: 150px;
    display: flex; align-items: center; justify-content: center; gap: 18px;
  }
  .card--dark .brand-mark { width: 34px; height: 34px; background: var(--red); }
  .card--dark .brand-name {
    font-size: 92px; font-weight: 500; color: var(--wordmark-grey);
    letter-spacing: 1px; line-height: 1;
  }
  /* Light side */
  .card--light {
    top: 656px; background: var(--paper);
  }
  .divider {
    position: absolute; left: 330px; top: 0; width: 64px; height: 434px;
  }
  .divider .cap-top { position: absolute; top: 0; left: 0; right: 0; height: 52px; background: var(--red); }
  .divider .core { position: absolute; top: 52px; left: 0; right: 0; height: 262px; background: var(--charcoal); }
  .divider .cap-bottom { position: absolute; bottom: 0; left: 0; right: 0; height: 120px; background: var(--red); }
  .card--light .brand {
    position: absolute; left: 48px; top: 150px;
    display: flex; align-items: center; gap: 10px;
  }
  .card--light .brand-mark { width: 16px; height: 16px; background: var(--red); }
  .card--light .brand-name {
    font-size: 44px; font-weight: 500; color: var(--wordmark-grey); line-height: 1;
  }
  .contact {
    position: absolute; right: 44px; top: 92px; width: 300px; text-align: right;
  }
  .contact .name {
    font-size: 32px; font-weight: 700; color: var(--red); line-height: 1.1;
  }
  .contact .rule {
    height: 3px; background: var(--red); margin: 6px 0 6px 0;
  }
  .contact .role {
    font-size: 19px; font-weight: 500; color: var(--text-grey);
  }
  .contact .details {
    list-style: none; margin-top: 34px;
    font-size: 16px; font-weight: 500; color: var(--text-grey); line-height: 2;
  }
</style>
</head>
<body>
<main class="sheet">
  <section class="card card--dark" aria-label="Card front, dark">
    <div class="brand">
      <span class="brand-mark"></span>
      <span class="brand-name">quorvela</span>
    </div>
    <div class="base-band"></div>
  </section>

  <section class="card card--light" aria-label="Card back, light">
    <div class="brand">
      <span class="brand-mark"></span>
      <span class="brand-name">quorvela</span>
    </div>
    <div class="divider">
      <div class="cap-top"></div>
      <div class="core"></div>
      <div class="cap-bottom"></div>
    </div>
    <div class="contact">
      <p class="name">Danielle Forsk</p>
      <div class="rule"></div>
      <p class="role">Licensee / Director</p>
      <ul class="details">
        <li>m. 0428 519 064</li>
        <li>e. danielle@quorvela.com.au</li>
        <li>quorvela.com.au</li>
      </ul>
    </div>
  </section>
</main>
</body>
</html>
```